Road Construction Company needs business cards

We would like a new business card designed for our business.

We're a road construction company based in Qld, Australia.

Can the business card please have the following information on it.

Name: Brent Malvoy
Position: General Manager
Phone: 0471 592 304
Email: Brent.malvoy@quendix.com.au
Address: 87 Harrowgate Ave, Pindarra, QLD, 4000
Website: www.quendix.com.au

Visually we'd like the card to be professional and simple.

Attached is our logo.

Our website is www.quendix.com.au

Target Market(s)

Men aged 25-60

Contact Information for Business Card

As listed in project description

Font styles to use
Serif

Requirements
Must have
• Large logo on back of card

```html
<!DOCTYPE html>
<html lang="en">
<head>
<meta charset="utf-8">
<title>Quendix Road Construction – Business Card</title>
<link href="https://fonts.googleapis.com/css2?family=Arimo:wght@400;700&display=swap" rel="stylesheet">
<style>
  :root {
    --page-bg: #e6e6e4;
    --card-white: #ffffff;
    --brand-blue: #0a55a6;
    --brand-blue-deep: #064a96;
    --accent-sky: #2fa0d8;
    --band-light: #3b86d2;
    --text-grey: #555a60;
    --rule-grey: #8a8f94;
  }
  * { box-sizing: border-box; margin: 0; padding: 0; }
  html, body {
    width: 1200px; height: 802px; overflow: hidden;
    background: var(--page-bg);
    font-family: "Arimo", Arial, sans-serif;
  }
  .stage { position: relative; width: 1200px; height: 802px; }
  .card {
    position: absolute; top: 252px;
    width: 520px; height: 297px;
    overflow: hidden;
    box-shadow: 0 6px 18px rgba(0,0,0,0.18);
  }
  /* Front */
  .card-front { left: 60px; background: var(--card-white); }
  .card-front .wave { position: absolute; inset: 0; }
  .front-wordmark {
    position: absolute; left: 30px; top: 150px;
    font-size: 34px; font-weight: 700; letter-spacing: 1px;
    color: var(--brand-blue);
  }
  .divider {
    position: absolute; left: 218px; top: 34px;
    width: 1px; height: 136px; background: var(--rule-grey);
  }
  .contact {
    position: absolute; left: 232px; top: 30px;
    color: var(--text-grey); font-size: 11px; line-height: 1.45;
  }
  .contact .name {
    color: var(--accent-sky); font-weight: 700; font-size: 16px;
    text-transform: uppercase; letter-spacing: 0.3px; line-height: 1.2;
  }
  .contact .role { font-size: 11.5px; margin-bottom: 8px; }
  .contact .address { margin-bottom: 7px; }
  .contact .line { display: flex; align-items: center; gap: 6px; }
  .contact .line svg { width: 10px; height: 10px; flex: none; }

  /* Back */
  .card-back { left: 620px; background: var(--brand-blue); }
  .card-back .band { position: absolute; inset: 0; }
  .back-wordmark {
    position: absolute; right: 40px; top: 42px;
    font-size: 40px; font-weight: 700; letter-spacing: 1.5px;
    color: #ffffff;
  }
</style>
</head>
<body>
<main class="stage">

  <section class="card card-front" aria-label="Business card front">
    <svg class="wave" viewBox="0 0 520 297" preserveAspectRatio="none" aria-hidden="true">
      <path d="M0,250 C150,245 330,228 408,184 C468,146 488,76 520,44 L520,58 C494,88 476,156 414,196 C336,242 150,258 0,264 Z" fill="var(--accent-sky)"/>
      <path d="M0,270 C150,264 340,250 420,204 C482,166 500,96 520,68 L520,297 L0,297 Z" fill="var(--brand-blue)"/>
    </svg>

    <div class="front-wordmark">QUENDIX</div>

    <div class="divider"></div>
    <div class="contact">
      <p class="name">Brent Malvoy</p>
      <p class="role">General Manager</p>
      <p class="address">87 Harrowgate Ave<br>Pindarra, QLD, 4000</p>
      <p class="line">
        <svg viewBox="0 0 10 10"><path d="M2,1 L4,1 L4.6,3 L3.4,3.8 C4,5.2 4.8,6 6.2,6.6 L7,5.4 L9,6 L9,8 C5,8.5 1.5,5 2,1 Z" fill="var(--accent-sky)"/></svg>
        0471 592 304
      </p>
      <p class="line">
        <svg viewBox="0 0 10 10"><rect x="1" y="2" width="8" height="6" fill="none" stroke="var(--accent-sky)" stroke-width="1"/><path d="M1,2 L5,5.5 L9,2" fill="none" stroke="var(--accent-sky)" stroke-width="1"/></svg>
        Brent.malvoy@quendix.com.au
      </p>
      <p class="line">
        <svg viewBox="0 0 10 10"><circle cx="5" cy="5" r="4" fill="none" stroke="var(--accent-sky)" stroke-width="1"/><path d="M1,5 H9 M5,1 C3,3.5 3,6.5 5,9 M5,1 C7,3.5 7,6.5 5,9" fill="none" stroke="var(--accent-sky)" stroke-width="0.8"/></svg>
        www.quendix.com.au
      </p>
    </div>
  </section>

  <section class="card card-back" aria-label="Business card back">
    <svg class="band" viewBox="0 0 520 297" preserveAspectRatio="none" aria-hidden="true">
      <defs>
        <linearGradient id="bandShade" x1="0" y1="0" x2="1" y2="0">
          <stop offset="0" stop-color="var(--brand-blue-deep)"/>
          <stop offset="0.7" stop-color="var(--band-light)"/>
          <stop offset="1" stop-color="var(--band-light)"/>
        </linearGradient>
      </defs>
      <path d="M0,110 L0,297 L250,297 L170,170 Z" fill="url(#bandShade)" opacity="0.9"/>
    </svg>
    <div class="back-wordmark">QUENDIX</div>
  </section>

</main>
</body>
</html>
```